High School Hockey Player Banners

I have 22 players that i need cropped out and added to a background with the school logo, player names and player numbers. I have uploaded all players photos w/ names and number on each file name. i have uploaded the Stone Creek Hornets school logo as well as an example of something that i like to give you inspiration. The finish size is 24" tall and 18" wide

```html
<!DOCTYPE html>
<html lang="en">
<head>
<meta charset="utf-8">
<title>Stone Creek Hornets – Player Banners</title>
<link href="https://fonts.googleapis.com/css2?family=Exo+2:ital,wght@0,900;1,900&display=swap" rel="stylesheet">
<style>
  :root{
    --page:#ffffff;
    --ink:#0b0f12;
    --red:#d4202a;
    --white:#ffffff;
    --sky-top:#0d1a1f;
    --sky-mid:#3f6c79;
    --sky-low:#a9d6e2;
    --sky-base:#eaf8fc;
    --ray-teal:#9fe3f2;
    --ray-gold:#e8c64a;
    --ray-red:#b2323a;
    --photo-a:#f4f1ee;
    --photo-b:#c93a34;
    --photo-c:#1d1d1f;
  }
  *{box-sizing:border-box;margin:0;padding:0}
  html,body{width:1000px;height:1200px;overflow:hidden;background:var(--page)}
  body{position:relative;font-family:"Exo 2",sans-serif}

  .banner{position:absolute;width:calc(588*var(--u));height:calc(786*var(--u));overflow:hidden}
  .banner--feature{--u:1px;--name-size:76;left:32px;top:207px}
  .banner--side{--u:0.524px;--name-size:70;left:650px;top:424px}

  .banner__backdrop{position:absolute;inset:0;width:100%;height:100%;display:block}

  .banner__number{
    position:absolute;left:calc(26*var(--u));top:calc(8*var(--u));
    font-size:calc(88*var(--u));font-weight:900;font-style:italic;line-height:1;
    color:var(--white);z-index:2;
  }

  .banner__name{
    position:absolute;left:calc(24*var(--u));bottom:calc(46*var(--u));
    writing-mode:vertical-rl;transform:rotate(180deg);
    font-size:calc(var(--name-size)*var(--u));font-weight:900;font-style:italic;line-height:1;
    letter-spacing:0;text-transform:uppercase;white-space:nowrap;
    color:var(--white);
    text-shadow:0 0 calc(10*var(--u)) rgba(0,0,0,.55);
    z-index:2;
  }

  .banner__photo{
    position:absolute;left:calc(120*var(--u));top:calc(68*var(--u));
    width:calc(440*var(--u));height:calc(700*var(--u));
    border-radius:calc(40*var(--u));
    background:
      radial-gradient(ellipse at 55% 30%, rgba(201,58,52,.55) 0%, rgba(201,58,52,0) 45%),
      radial-gradient(ellipse at 50% 55%, var(--photo-a) 0%, rgba(244,241,238,.7) 45%, rgba(244,241,238,0) 72%),
      radial-gradient(ellipse at 55% 92%, rgba(29,29,31,.35) 0%, rgba(29,29,31,0) 40%);
  }

  .banner__team{
    position:absolute;right:calc(18*var(--u));bottom:calc(24*var(--u));
    width:calc(200*var(--u));
    text-align:center;text-transform:uppercase;
    font-size:calc(30*var(--u));font-weight:900;line-height:1.02;
    color:var(--ink);
  }
</style>
</head>
<body>

<section class="banner banner--feature" aria-label="Player banner, number 12">
  <svg class="banner__backdrop" viewBox="0 0 588 786" preserveAspectRatio="none" aria-hidden="true">
    <defs>
      <linearGradient id="skyA" x1="0" y1="0" x2="0" y2="1">
        <stop offset="0" stop-color="var(--sky-top)"/>
        <stop offset=".32" stop-color="var(--sky-mid)"/>
        <stop offset=".68" stop-color="var(--sky-low)"/>
        <stop offset="1" stop-color="var(--sky-base)"/>
      </linearGradient>
    </defs>
    <rect width="588" height="786" fill="url(#skyA)"/>
    <polygon points="588,40 588,70 300,420 270,420" fill="var(--ray-teal)" opacity=".45"/>
    <polygon points="588,150 588,175 380,420 355,420" fill="var(--ray-gold)" opacity=".55"/>
    <polygon points="560,0 588,0 400,260 372,260" fill="var(--ray-red)" opacity=".45"/>
    <polygon points="588,230 588,320 430,520 380,520" fill="var(--ray-teal)" opacity=".3"/>
    <polygon points="0,0 200,0 95,105 0,105" fill="var(--ink)"/>
    <polygon points="200,0 226,0 121,105 95,105" fill="var(--red)"/>
  </svg>
  <div class="banner__photo" role="img" aria-label="Cut-out action photo of the player skating with his stick"></div>
  <div class="banner__number">12</div>
  <div class="banner__name">Colin Marsh</div>
  <div class="banner__team">Stone Creek<br>Hornets</div>
</section>

<section class="banner banner--side" aria-label="Player banner, number 1">
  <svg class="banner__backdrop" viewBox="0 0 588 786" preserveAspectRatio="none" aria-hidden="true">
    <defs>
      <linearGradient id="skyB" x1="0" y1="0" x2="0" y2="1">
        <stop offset="0" stop-color="var(--sky-top)"/>
        <stop offset=".32" stop-color="var(--sky-mid)"/>
        <stop offset=".68" stop-color="var(--sky-low)"/>
        <stop offset="1" stop-color="var(--sky-base)"/>
      </linearGradient>
    </defs>
    <rect width="588" height="786" fill="url(#skyB)"/>
    <polygon points="588,40 588,70 300,420 270,420" fill="var(--ray-teal)" opacity=".45"/>
    <polygon points="588,150 588,175 380,420 355,420" fill="var(--ray-gold)" opacity=".55"/>
    <polygon points="560,0 588,0 400,260 372,260" fill="var(--ray-red)" opacity=".45"/>
    <polygon points="588,230 588,320 430,520 380,520" fill="var(--ray-teal)" opacity=".3"/>
    <polygon points="0,0 200,0 95,105 0,105" fill="var(--ink)"/>
    <polygon points="200,0 226,0 121,105 95,105" fill="var(--red)"/>
  </svg>
  <div class="banner__photo" role="img" aria-label="Cut-out photo of the goalie in a ready stance"></div>
  <div class="banner__number">1</div>
  <div class="banner__name">Ethan Brooks</div>
  <div class="banner__team">Stone Creek<br>Hornets</div>
</section>

</body>
</html>
```